TALLOWBROOK FREIGHT & PLANT HIRE NEEDS A FLYER

WE NEED A FLYER FOR OUR COMPANY <br/>WE SPECIALISE IN ROAD BUILDING AND MAINTENANCE, GENERAL EARTHWORK DAM REPAIRS & DESILTING, FENCE CLEARING, FIRE BREAKS, GRAVEL SOURCE AND DELIVERY GENERAL FREIGHT STEEL HAY LICK AND MCHINERY. <br/><br/>I HAVE UPLOAD A FILE THAT I LIKE AND WOULD LIKE SOMETHING THE SAME IF POSSIBLE. AND LOGO TO GO WITH IT.

```html
<!DOCTYPE html>
<html lang="en">
<head>
<meta charset="utf-8">
<title>Tallowbrook Freight &amp; Plant Hire Flyer</title>
<link rel="stylesheet" href="https://fonts.googleapis.com/css2?family=Montserrat:wght@500;600;700&display=swap">
<style>
  :root {
    --yellow: #fbb01a;
    --orange: #f29a12;
    --charcoal: #333335;
    --white: #ffffff;
    --backdrop: #ececec;
  }
  * { margin: 0; padding: 0; box-sizing: border-box; }
  html, body {
    width: 1200px;
    height: 2264px;
    overflow: hidden;
    background: var(--backdrop);
    font-family: "Montserrat", sans-serif;
  }
  .flyer {
    position: absolute;
    left: 0;
    top: 284px;
    width: 1200px;
    height: 1696px;
    box-shadow: 0 6px 24px rgba(0,0,0,0.18);
  }
  .flyer-shapes {
    position: absolute;
    inset: 0;
    width: 100%;
    height: 100%;
  }
  .line {
    position: absolute;
    left: 0;
    width: 100%;
    text-align: center;
    text-transform: uppercase;
    white-space: nowrap;
  }
  .tagline {
    top: 66px;
    font-size: 38px;
    line-height: 50px;
    font-weight: 600;
    color: var(--charcoal);
  }
  .brand-name {
    top: 300px;
    color: var(--charcoal);
    font-weight: 700;
    line-height: 1.1;
  }
  .brand-name .main { display: block; font-size: 100px; }
  .brand-name .sub { display: block; font-size: 60px; }
  .brand-name .suffix { display: block; font-size: 40px; }
  .section-heading {
    font-size: 40px;
    line-height: 50px;
    font-weight: 600;
    color: var(--orange);
  }
  .heading-services { top: 760px; }
  .heading-machinery { top: 1089px; }
  .list {
    font-size: 32px;
    font-weight: 600;
    color: var(--white);
  }
  .list-services { top: 835px; line-height: 49px; }
  .list-machinery { top: 1174px; line-height: 50px; }
  .contact-names {
    top: 1453px;
    font-size: 34px;
    line-height: 44px;
    font-weight: 600;
    color: var(--charcoal);
  }
  .contact-phone {
    top: 1506px;
    font-size: 56px;
    line-height: 60px;
    font-weight: 700;
    color: var(--charcoal);
    letter-spacing: 1px;
  }
  .contact-email {
    top: 1570px;
    font-size: 32px;
    line-height: 44px;
    font-weight: 600;
    color: var(--charcoal);
    text-transform: none;
  }
  .contact-email svg {
    width: 40px;
    height: 28px;
    vertical-align: -4px;
  }
</style>
</head>
<body>
  <main class="flyer">
    <svg class="flyer-shapes" viewBox="0 0 861 1217" preserveAspectRatio="none" aria-hidden="true">
      <rect width="861" height="1217" fill="var(--charcoal)"/>
      <polygon points="0,0 861,0 861,55 823,118 37,118 0,55" fill="var(--yellow)"/>
      <rect x="0" y="168" width="861" height="335" fill="var(--white)"/>
      <polygon points="0,950 48,1022 813,1022 861,955 861,1120 790,1217 75,1217 0,1125" fill="var(--yellow)"/>
    </svg>

    <p class="line tagline">For all you freight and plant hire needs!</p>

    <h1 class="line brand-name">
      <span class="main">TALLOWBROOK</span>
      <span class="sub">FREIGHT &amp; PLANT HIRE</span>
      <span class="suffix">PTY LTD</span>
    </h1>

    <h2 class="line section-heading heading-services">Specialising in:</h2>
    <p class="line list list-services">
      Road building and maintenance • General<br>
      earthworks • Dam repairs &amp; desilting • Fence<br>
      clearing • Fire breaks • Gravel source &amp; delivery<br>
      General freight • Steel • Lick • Hay • Machinery
    </p>

    <h2 class="line section-heading heading-machinery">Current machinery avaiable:</h2>
    <p class="line list list-machinery">
      Grader • Loader &amp; stick rack • Rollers<br>
      Dozer • Water trucks • Side tippers • Prime<br>
      Movers • Forklift • Skid steer loader • Flat<br>
      Tops • Drop deck
    </p>

    <p class="line contact-names">Mark &amp; Jessica Dalewood</p>
    <p class="line contact-phone">0455201847</p>
    <p class="line contact-email">
      <svg viewBox="0 0 40 28" aria-label="Email"><rect x="1" y="1" width="38" height="26" fill="var(--charcoal)"/><polyline points="3,4 20,16 37,4" fill="none" stroke="var(--yellow)" stroke-width="3"/></svg>: jessicadalewood@mailbox.com
    </p>
  </main>
</body>
</html>
```